Powerpoint visual improvements

I need a cover page, and our beliefs page and differentiating factors page / graphic design for our presentation. For the cover page I would just like an attractive design that incorporate our architectural concept with columns and potentially our logo. For the beliefs page I just want a more attractive presentatoin of the concepts. For the differentiating factors page I want a graphic that captures the points about how we are different from competitors. I have used the attached content to date, but I think it can be improved. The text is included in the graphic and I would also like to make sure the firm logo is incorporated.

Target Market(s)

Individual and institutional investors.

Industry/Entity Type

Investment Advisory

Requirements
Must have
• Our corporate colors are generally RGB 145,148,149; 66,68,76; 0,0,153; and 0,63,127. Our logo is attached. Our primary font is Georgia. Our website is www.VorlineCP.com. The key pages are www.VorlineCP.com/beliefs and www.VorlineCP.com/value we are trying to capture in a presentation. We also need a new presentation cover. Use the website as a reference for the type of imagery we like.

```html
<!DOCTYPE html>
<html lang="en">
<head>
<meta charset="utf-8">
<title>Aldane – Differentiating Factors</title>
<link rel="stylesheet" href="https://fonts.googleapis.com/css2?family=Gelasio:wght@400&display=swap">
<style>
  :root {
    --bg-light: #f1f3f4;
    --bg-mid: #dfe3e4;
    --bg-corner: #6f9593;
    --slate: #46647a;
    --gold: #fdbf47;
    --coral: #f26e63;
    --graphite: #6b6c70;
    --teal: #0bb5a2;
    --azure: #2899d8;
    --core: #e8ebec;
    --brand-grey: #97999b;
    --ink: #111111;
    --label: #ffffff;
  }
  html, body {
    margin: 0;
    padding: 0;
    overflow: hidden;
  }
  .slide {
    position: relative;
    width: 1200px;
    height: 686px;
    overflow: hidden;
    background:
      radial-gradient(ellipse 420px 360px at 0% 100%, var(--bg-corner) 0%, rgba(111,149,147,0) 100%),
      radial-gradient(ellipse 380px 320px at 100% 0%, var(--bg-corner) 0%, rgba(111,149,147,0) 100%),
      radial-gradient(ellipse 900px 600px at 55% 50%, var(--bg-light) 0%, var(--bg-mid) 100%);
    font-family: "Gelasio", Georgia, serif;
  }
  .factor-wheel {
    position: absolute;
    inset: 0;
    width: 1200px;
    height: 686px;
  }
  .segment--communication { fill: var(--slate); }
  .segment--investors { fill: var(--gold); }
  .segment--portfolio { fill: var(--coral); }
  .segment--operations { fill: var(--graphite); }
  .segment--fees { fill: var(--teal); }
  .segment--research { fill: var(--azure); }
  .core { fill: var(--core); }
  .factor-label {
    fill: var(--label);
    font-family: "Gelasio", Georgia, serif;
    font-size: 18px;
    letter-spacing: 2.4px;
    text-anchor: middle;
  }
  .icon { fill: var(--ink); }
  .icon-stroke { fill: none; stroke: var(--ink); stroke-width: 3; stroke-linecap: round; }
  .brand-name {
    fill: var(--brand-grey);
    font-family: "Gelasio", Georgia, serif;
    font-size: 44px;
    text-anchor: middle;
  }
  .brand-dot { fill: var(--brand-grey); }
</style>
</head>
<body>
<main class="slide">
  <svg class="factor-wheel" viewBox="0 0 1400 800" role="img" aria-label="Six differentiating factors arranged around the Aldane name">
    <polygon class="segment segment--communication" points="470,65 672,65 575,242 490,388 385,215"/>
    <polygon class="segment segment--investors" points="672,65 850,65 950,242 575,242"/>
    <polygon class="segment segment--portfolio" points="750,242 950,242 1037,390 935,568 835,390"/>
    <polygon class="segment segment--operations" points="835,390 935,568 850,717 648,717 750,540"/>
    <polygon class="segment segment--fees" points="372,540 750,540 648,717 470,717"/>
    <polygon class="segment segment--research" points="385,215 490,388 575,540 372,540 285,390"/>
    <polygon class="core" points="490,390 575,242 750,242 835,390 750,540 575,540"/>

    <g class="brand">
      <circle class="brand-dot" cx="600" cy="390" r="12"/>
      <text class="brand-name" x="680" y="405">Aldane</text>
    </g>

    <!-- antenna -->
    <g class="icon-group">
      <path class="icon" d="M503 118 L492 153 H498 L503 136 L508 153 H514 Z"/>
      <circle class="icon" cx="503" cy="118" r="4"/>
      <path class="icon-stroke" d="M493 110 A14 14 0 0 0 493 126 M513 110 A14 14 0 0 1 513 126 M486 104 A22 22 0 0 0 486 132 M520 104 A22 22 0 0 1 520 132"/>
    </g>
    <text class="factor-label" x="503" y="188">Transparent</text>
    <text class="factor-label" x="503" y="208">Communication</text>

    <!-- money bag -->
    <g class="icon-group">
      <path class="icon" d="M740 100 C722 112 724 140 750 140 C776 140 778 112 760 100 Z"/>
      <rect class="icon" x="740" y="88" width="20" height="10" rx="3"/>
      <rect class="icon" x="760" y="92" width="12" height="8" rx="2"/>
    </g>
    <text class="factor-label" x="755" y="174">Experienced</text>
    <text class="factor-label" x="755" y="194">Investors</text>

    <!-- puzzle -->
    <g class="icon-group">
      <rect class="icon" x="895" y="298" width="44" height="44"/>
      <rect x="917" y="300" width="20" height="20" fill="#ffffff"/>
      <rect x="897" y="320" width="20" height="20" fill="#ffffff"/>
      <circle class="icon" cx="927" cy="320" r="5"/>
      <circle class="icon" cx="907" cy="320" r="5"/>
    </g>
    <text class="factor-label" x="925" y="378">Independant</text>
    <text class="factor-label" x="925" y="398">Portfolio</text>
    <text class="factor-label" x="925" y="418">Construction</text>

    <!-- speaker -->
    <g class="icon-group">
      <path class="icon" d="M783 530 H792 L806 518 V560 L792 548 H783 Z"/>
      <path class="icon-stroke" d="M814 530 A12 12 0 0 1 814 548 M820 522 A22 22 0 0 1 820 556 M826 514 A32 32 0 0 1 826 564"/>
    </g>
    <text class="factor-label" x="803" y="596">Sound</text>
    <text class="factor-label" x="803" y="616">Operation</text>
    <text class="factor-label" x="803" y="636">Platform</text>

    <!-- magnifier with rising chart -->
    <g class="icon-group">
      <circle cx="568" cy="590" r="15" fill="#ffffff" stroke="#111111" stroke-width="5"/>
      <path class="icon-stroke" d="M556 602 L540 620" style="stroke-width:6"/>
      <path d="M560 596 L566 589 L570 592 L577 583" fill="none" stroke="#0bb5a2" stroke-width="2"/>
    </g>
    <text class="factor-label" x="556" y="651">Proactive Total</text>
    <text class="factor-label" x="556" y="671">Fee Management</text>

    <!-- magnifier with bars -->
    <g class="icon-group">
      <circle cx="400" cy="364" r="16" fill="#ffffff" stroke="#111111" stroke-width="5"/>
      <path class="icon-stroke" d="M412 376 L428 390" style="stroke-width:6"/>
      <rect class="icon" x="392" y="364" width="4" height="9"/>
      <rect class="icon" x="398" y="358" width="4" height="15"/>
      <rect class="icon" x="404" y="361" width="4" height="12"/>
    </g>
    <text class="factor-label" x="418" y="424">Institutional</text>
    <text class="factor-label" x="418" y="444">Research Process</text>
  </svg>
</main>
</body>
</html>
```